Business Card Design

Lotside Ledger is an online automotive resource on a national scale specifically targeting lease purchases for new cars. Our Online and app platform allow prospective lease clients to scan a window sticker while at a franchise dealership and instantly receive a lease quote at what we call the sweet spot. Lotside Ledger offers price transparency during the lease process to allow average people the confidence in the lease process and takes away any fear of the big franchise dealers.
Lotside ledger allows ordinary lease customers to know they are getting a low price lease and not overpaying. Never overpay again

Industry/Entity Type

Automotive

Contact Information for Business Card

Lotside Ledger
Marcus Todwell (President of operations)
Phone: 888-302-7716
Cell: 561-448-2053

```html
<!DOCTYPE html>
<html lang="en">
<head>
<meta charset="utf-8">
<title>Lotside Ledger — Business Card</title>
<link rel="stylesheet" href="https://fonts.googleapis.com/css2?family=Open+Sans:wght@400;700;800&display=swap">
<style>
  :root {
    --stage: #6f6f6f;
    --card: #262626;
    --ink-light: #ffffff;
    --ink-dark: #111111;
    --band: #ffffff;
  }
  * { margin: 0; padding: 0; box-sizing: border-box; }
  html, body {
    width: 1200px;
    height: 1000px;
    overflow: hidden;
    background: var(--stage);
    font-family: "Open Sans", Arial, sans-serif;
  }
  .sheet {
    position: relative;
    width: 1200px;
    height: 1000px;
  }
  .card {
    position: absolute;
    left: 240px;
    width: 720px;
    height: 412px;
    background: var(--card);
    overflow: hidden;
  }
  .card--back { top: 50px; }
  .card--front { top: 538px; }

  /* Back: brand name */
  .brand {
    position: absolute;
    inset: 0;
    display: flex;
    align-items: center;
    justify-content: center;
    gap: 22px;
  }
  .brand__dot {
    width: 46px;
    height: 46px;
    border-radius: 50%;
    background: var(--ink-light);
  }
  .brand__name {
    color: var(--ink-light);
    font-weight: 800;
    font-size: 64px;
    line-height: 0.95;
    text-transform: uppercase;
    letter-spacing: -1px;
  }

  /* Front: identity */
  .identity {
    position: absolute;
    right: 130px;
    top: 120px;
    text-align: right;
  }
  .identity__name {
    color: var(--ink-light);
    font-weight: 700;
    font-size: 22px;
    letter-spacing: 1px;
    text-transform: uppercase;
  }
  .identity__title {
    color: var(--ink-light);
    font-weight: 400;
    font-size: 17px;
    margin-top: 6px;
    text-transform: uppercase;
  }
  .identity__rule {
    position: absolute;
    left: 612px;
    top: 128px;
    width: 2px;
    height: 60px;
    background: var(--ink-light);
  }

  /* Front: contact band */
  .contact-band {
    position: absolute;
    left: 0;
    right: 0;
    top: 255px;
    height: 100px;
    background: var(--band);
    display: flex;
    align-items: center;
    padding-left: 100px;
  }
  .contact {
    display: flex;
    align-items: center;
    gap: 18px;
    width: 340px;
  }
  .contact__tag {
    width: 28px;
    height: 28px;
    background: var(--ink-dark);
    color: var(--ink-light);
    font-weight: 700;
    font-size: 14px;
    display: flex;
    align-items: center;
    justify-content: center;
  }
  .contact__number {
    color: var(--ink-dark);
    font-size: 18px;
    letter-spacing: 0.5px;
  }
</style>
</head>
<body>
  <main class="sheet">
    <section class="card card--back" aria-label="Business card, brand side">
      <div class="brand">
        <span class="brand__dot"></span>
        <span class="brand__name">Lotside<br>Ledger</span>
      </div>
    </section>

    <section class="card card--front" aria-label="Business card, contact side">
      <div class="identity">
        <p class="identity__name">Marcus Todwell</p>
        <p class="identity__title">President of Operations</p>
      </div>
      <span class="identity__rule"></span>

      <div class="contact-band">
        <div class="contact">
          <span class="contact__tag">P</span>
          <span class="contact__number">888-302-7716</span>
        </div>
        <div class="contact">
          <span class="contact__tag">C</span>
          <span class="contact__number">561-448-2053</span>
        </div>
      </div>
    </section>
  </main>
</body>
</html>
```